Hair dresser flyer for Air conditioning heat pumps A5

We require a flyer that is selling the benifits of air conditioning heat pumps which cools in summer and efficently heats in winter. Colour should be white background. Red and blue from logo to represent the Air conditioning Heat pump does heating and cooling and energy effient.

Target Market(s)

Hairdressor, Salons , barbers ,

Colors
0054AA
0677BA
7BADD7
CADEEF
E8F1F8
EB3D1F
EC4F4E
F09395
F8D3D4
FCEDEE

Requirements
Must have
• Cost from

```html
<!DOCTYPE html>
<html lang="en">
<head>
<meta charset="utf-8">
<title>Harlow – Air Conditioning Heat Pumps for Salons</title>
<link rel="stylesheet" href="https://fonts.googleapis.com/css2?family=Poppins:wght@400;500;600;700;800&display=swap">
<style>
  :root {
    --blue: #34a9df;
    --orange: #e9501e;
    --ink: #0d0d0d;
    --paper: #ffffff;
  }
  * { margin: 0; padding: 0; box-sizing: border-box; }
  html, body { width: 846px; height: 1200px; overflow: hidden; background: var(--paper); }
  body { font-family: "Poppins", sans-serif; color: var(--ink); }
  .flyer { position: relative; width: 846px; height: 1200px; overflow: hidden; background: var(--paper); }

  .hero-photo { position: absolute; top: 0; left: 0; width: 846px; height: 520px; }

  .brand { position: absolute; left: 55px; top: 48px; }
  .brand-name { display: block; font-weight: 800; font-size: 68px; line-height: 1; letter-spacing: -1.5px; color: var(--ink); }

  .headline { position: absolute; left: 55px; top: 192px; }
  .headline-save { font-weight: 800; font-size: 74px; line-height: 1; letter-spacing: 1px; }
  .headline-sub { font-weight: 700; font-size: 28.5px; line-height: 34px; margin-top: -2px; }
  .hot { color: var(--orange); }
  .cool { color: var(--blue); }

  .offer { position: absolute; left: 54px; top: 372px; font-weight: 700; font-size: 27px; line-height: 34px; }
  .offer .price { color: var(--orange); }

  .benefits { position: absolute; left: 55px; top: 468px; width: 760px; display: grid; grid-template-columns: 364px 396px; row-gap: 10px; list-style: none; }
  .benefit { display: flex; align-items: center; gap: 6px; font-size: 21px; height: 31px; white-space: nowrap; }
  .tick { width: 32px; height: 32px; flex: none; }

  .gallery { position: absolute; left: 0; top: 652px; width: 846px; height: 188px; }
  .colour-bar { position: absolute; left: 0; top: 840px; width: 846px; height: 12px; display: flex; }
  .colour-bar .cool-half { flex: 1; background: var(--blue); }
  .colour-bar .warm-half { flex: 1; background: var(--orange); }

  .body-copy { position: absolute; left: 53px; top: 872px; width: 790px; font-size: 19.6px; line-height: 24.2px; letter-spacing: 0.15px; white-space: nowrap; }
  .body-copy p + p { margin-top: 24px; }
</style>
</head>
<body>
<main class="flyer">

  <svg class="hero-photo" viewBox="0 0 846 520">
    <defs>
      <linearGradient id="roomTone" x1="0" y1="0" x2="0.4" y2="1">
        <stop offset="0" stop-color="#8b8e92"/>
        <stop offset="0.45" stop-color="#a3a6aa"/>
        <stop offset="0.7" stop-color="#cfaaa4"/>
        <stop offset="1" stop-color="#d8b3ad"/>
      </linearGradient>
    </defs>
    <path role="img" aria-label="Photo of a wall-mounted air conditioning unit in a pink salon interior"
          d="M392 0 C450 20 480 90 492 160 C505 230 525 280 590 300 C650 318 720 320 780 350 C815 370 838 420 846 470 L846 0 Z"
          fill="url(#roomTone)"/>
    <path d="M398 12 C452 38 480 100 490 165 C502 236 522 288 588 308 C650 328 722 330 782 360 C818 380 840 430 846 512"
          fill="none" stroke="var(--blue)" stroke-width="5"/>
  </svg>

  <header class="brand">
    <span class="brand-name">Harlow</span>
  </header>

  <section class="headline">
    <h1 class="headline-save">SAVE £££</h1>
    <p class="headline-sub">on your Shops <span class="hot">Heating</span> costs<br>And stay <span class="cool">Cool</span> in the Summer</p>
  </section>

  <h2 class="offer">Energy- Efficient Air Conditioning Heat Pumps<br>installed from <span class="price">£1750 + Vat</span></h2>

  <ul class="benefits">
    <li class="benefit"><svg class="tick" viewBox="0 0 32 32"><path d="M24 8 A13 13 0 1 0 28.5 17" fill="none" stroke="var(--blue)" stroke-width="2.2" stroke-linecap="round"/><path d="M9 15 L15 22 L31 2" fill="none" stroke="var(--blue)" stroke-width="2.6" stroke-linecap="round" stroke-linejoin="round"/></svg>Cools in Summer</li>
    <li class="benefit"><svg class="tick" viewBox="0 0 32 32"><path d="M24 8 A13 13 0 1 0 28.5 17" fill="none" stroke="var(--orange)" stroke-width="2.2" stroke-linecap="round"/><path d="M9 15 L15 22 L31 2" fill="none" stroke="var(--orange)" stroke-width="2.6" stroke-linecap="round" stroke-linejoin="round"/></svg>Reduce cancellation in Summer</li>
    <li class="benefit"><svg class="tick" viewBox="0 0 32 32"><path d="M24 8 A13 13 0 1 0 28.5 17" fill="none" stroke="var(--orange)" stroke-width="2.2" stroke-linecap="round"/><path d="M9 15 L15 22 L31 2" fill="none" stroke="var(--orange)" stroke-width="2.6" stroke-linecap="round" stroke-linejoin="round"/></svg>Efficient Heats in Winter</li>
    <li class="benefit"><svg class="tick" viewBox="0 0 32 32"><path d="M24 8 A13 13 0 1 0 28.5 17" fill="none" stroke="var(--blue)" stroke-width="2.2" stroke-linecap="round"/><path d="M9 15 L15 22 L31 2" fill="none" stroke="var(--blue)" stroke-width="2.6" stroke-linecap="round" stroke-linejoin="round"/></svg>Filters and cleans the air</li>
    <li class="benefit"><svg class="tick" viewBox="0 0 32 32"><path d="M24 8 A13 13 0 1 0 28.5 17" fill="none" stroke="var(--blue)" stroke-width="2.2" stroke-linecap="round"/><path d="M9 15 L15 22 L31 2" fill="none" stroke="var(--blue)" stroke-width="2.6" stroke-linecap="round" stroke-linejoin="round"/></svg>More Productive staff</li>
    <li class="benefit"><svg class="tick" viewBox="0 0 32 32"><path d="M24 8 A13 13 0 1 0 28.5 17" fill="none" stroke="var(--orange)" stroke-width="2.2" stroke-linecap="round"/><path d="M9 15 L15 22 L31 2" fill="none" stroke="var(--orange)" stroke-width="2.6" stroke-linecap="round" stroke-linejoin="round"/></svg>Reduced allergens &amp; Bugs</li>
    <li class="benefit"><svg class="tick" viewBox="0 0 32 32"><path d="M24 8 A13 13 0 1 0 28.5 17" fill="none" stroke="var(--orange)" stroke-width="2.2" stroke-linecap="round"/><path d="M9 15 L15 22 L31 2" fill="none" stroke="var(--orange)" stroke-width="2.6" stroke-linecap="round" stroke-linejoin="round"/></svg>Increased Sales</li>
    <li class="benefit"><svg class="tick" viewBox="0 0 32 32"><path d="M24 8 A13 13 0 1 0 28.5 17" fill="none" stroke="var(--blue)" stroke-width="2.2" stroke-linecap="round"/><path d="M9 15 L15 22 L31 2" fill="none" stroke="var(--blue)" stroke-width="2.6" stroke-linecap="round" stroke-linejoin="round"/></svg>Reduce Humidity</li>
  </ul>

  <svg class="gallery" viewBox="0 0 846 188">
    <defs>
      <linearGradient id="salonTone" x1="0" y1="0" x2="0" y2="1">
        <stop offset="0" stop-color="#a8a6a2"/><stop offset="0.5" stop-color="#d6d2cc"/><stop offset="1" stop-color="#6b6864"/>
      </linearGradient>
      <linearGradient id="flowerTone" x1="0" y1="0" x2="1" y2="1">
        <stop offset="0" stop-color="#e6dcdd"/><stop offset="0.5" stop-color="#d9a9b6"/><stop offset="1" stop-color="#cfc6c4"/>
      </linearGradient>
      <linearGradient id="unitTone" x1="0" y1="0" x2="1" y2="1">
        <stop offset="0" stop-color="#e9ecee"/><stop offset="0.35" stop-color="#2a2b2d"/><stop offset="1" stop-color="#141516"/>
      </linearGradient>
    </defs>
    <path role="img" aria-label="Photo of a barber salon interior with a ceiling cassette unit" d="M0 0 H256 Q262 100 252 188 H0 Z" fill="url(#salonTone)"/>
    <path role="img" aria-label="Photo of a round ceiling cassette above a floral salon display" d="M264 0 H572 Q562 100 568 188 H260 Q270 100 264 0 Z" fill="url(#flowerTone)"/>
    <path role="img" aria-label="Photo of a black wall-mounted air conditioning unit" d="M580 0 H846 V188 H576 Q570 100 580 0 Z" fill="url(#unitTone)"/>
  </svg>
  <div class="colour-bar"><span class="cool-half"></span><span class="warm-half"></span></div>

  <section class="body-copy">
    <p>Air Conditioning Heat Pumps creates the ideal environment all year round<br>for staff to be at there most productive and for consumers to spend more<br>time and, accordingly, more money.</p>
    <p>Modern Air Conditioning Heat pumps are one of the most energy efficient<br>forms of heating available and ideal for those looking for a simple cost<br>effective way to heat and cool the space. They are easy to install&nbsp; and<br>operate and can quickly provide with the comfort you need.</p>
    <p>Reduce cancelations and absences in the warm summer months with<br>Cooling mode. With the warms temperatures inside hairdressers and<br>salons and clients not wanting to sit in somewhere with extreme heat.</p>
  </section>

</main>
</body>
</html>
```